The Logo is

Run ♪ Loud ... you can see it on the website (see below)

NB black background, font is light silver, the music character ♪ is in RED and a larger font size than the text characters.

FRONT

1. Run ♪ Loud Magazine

I run an internet magazine called Run ♪ Loud Magazine

www.runloudzine.example

NB the music character ♪ is in RED and a larger font size than the text characters.

We "shoot" rock bands and then write up articles about them with photographs.

REVERSE

2. Run ♪ Loud Radio

I run a radio program called

Run ♪ Loud Radio

www.runloudzine.example/run-loud-radio/

It's a program where we play tracks by the artists we have just seen and photographed and those that we are going to see.

3. General

It would make sense to have Run ♪ Loud Magazine on one side of the card and Run ♪ Radio on the reverse.

Information on the front does not need to be repeated on the reverse but clearlt there should be a "common theme" but not necessarily a mirror effect ... as long as the Reverse side complements the Front.

I don't want to use the proforma standard Cardforge designs.

I am comfortable with wild design as this is rock n roll ... so I am not looking for geometrics or nice pastoral scenes, pretty girls or boys.

Attitude, grunt ... sweat and action ... full colour.

The words "Run Loud" may provide some opportunity for design but I have an open mind.

To get a feel for what I am looking for, I strongly suggest you have a good look around the website

www.runloudzine.example

Finally - I'd be delighted for you to use any of my own photographs - now there's a clue - which you can see on the website - and yes, you are allowed to crop them or "distort" them if that makes sense. If you want me to send a high res image, let me know.

Good luck ...

pete morrow
editor@runloudzine.example
+61 4 2735 8819
Updates

We are coming down to the wire ... I am very pleased with all of the submissions.  We are down to a shortlist of about 6 ... and I will provide advice over the next 24 hours or so to help you individually.  For everyone ... please note the following

The title has been standardised for both sides of the card to "Chief" ... so please change the word "Editor" or "Presenter" or "DJ" or "Publisher" to the one single title for both radio and magazine as just simply "Chief".

The email address is to be "chief@runloudzine.example".

Any private emails please continue to send them to editor@runloudzine.example

If you are thinking of incorporating a tag line (that would be nice) it should be

"Music With Attitude"

Thanks .. I hope that helps .... and you know, good luck.

pete

Target Market(s)

Bands, singers, performers, public relations agencies

Industry/Entity Type

Internet

Contact Information for Business Card

Pete Morrow
Editor

P.O. Box 5817
North Turramurra
NSW 2074
Ph 042 735 8819

Requirements
Must have
• Kavel,

Here are the two images ...

one can replace the man with his tongue out

the other can replace to main character on the other side of the card.

You can write to me directly

pete

```html
<!DOCTYPE html>
<html lang="en">
<head>
<meta charset="utf-8">
<title>Run Loud – Business Cards</title>
<link rel="stylesheet" href="https://fonts.googleapis.com/css2?family=Tenor+Sans&family=Cantarell:wght@400;700&display=swap">
<style>
  :root {
    --stage-light: #ffffff;
    --stage-dark: #bdbcbd;
    --card-black: #231f20;
    --vinyl-red: #ed1c24;
    --name-red: #b01e23;
    --silver: #d4d4d4;
    --white: #ffffff;
  }
  html, body {
    margin: 0;
    padding: 0;
    width: 1200px;
    height: 900px;
    overflow: hidden;
  }
  body {
    position: relative;
    background: radial-gradient(ellipse 62% 60% at 50% 50%, var(--stage-light) 55%, var(--stage-dark) 100%);
    font-family: "Cantarell", sans-serif;
  }
  .card {
    position: absolute;
    left: 327px;
    width: 546px;
    height: 316px;
    display: block;
  }
  .card--magazine { top: 121px; }
  .card--radio { top: 480px; }
  .card-bg { fill: var(--card-black); }
  .art-frame { fill: none; stroke: var(--vinyl-red); stroke-width: 2.5; }
  .stop-red { stop-color: var(--vinyl-red); }
  .stop-dark { stop-color: var(--card-black); }
  .wordmark {
    font-family: "Tenor Sans", sans-serif;
    font-size: 60px;
    font-variant: small-caps;
    letter-spacing: 7px;
    fill: var(--silver);
  }
  .wordmark-dot { fill: var(--name-red); }
  .division {
    font-family: "Tenor Sans", sans-serif;
    fill: var(--silver);
  }
  .division--magazine { font-size: 18px; letter-spacing: 7px; }
  .division--radio { font-size: 23px; letter-spacing: 14px; }
  .contact-name, .contact-title {
    font-family: "Cantarell", sans-serif;
    font-weight: 700;
    font-size: 15.5px;
    fill: var(--name-red);
  }
  .contact-line {
    font-family: "Cantarell", sans-serif;
    font-size: 15.5px;
    fill: var(--white);
  }
</style>
</head>
<body>

<svg class="card card--magazine" viewBox="0 0 646 374" aria-label="Run Loud Magazine business card, front">
  <defs>
    <radialGradient id="art-tone-front" cx="0" cy="194" r="290" gradientUnits="userSpaceOnUse">
      <stop offset="0" class="stop-red"/>
      <stop offset="0.35" class="stop-red" stop-opacity="0.75"/>
      <stop offset="0.8" class="stop-dark"/>
      <stop offset="1" class="stop-dark"/>
    </radialGradient>
  </defs>
  <rect class="card-bg" width="646" height="374"/>
  <rect x="0" y="0" width="283" height="374" fill="url(#art-tone-front)" role="img" aria-label="Illustration of overlapping vinyl records in black and red"/>
  <path class="art-frame" d="M283 1 L1 1 L1 373 L270 373"/>

  <circle class="wordmark-dot" cx="272" cy="95" r="12"/>
  <text class="wordmark" x="622" y="112" text-anchor="end">Run Loud</text>
  <text class="division division--magazine" x="624" y="147" text-anchor="end">MAGAZINE</text>

  <text class="contact-name" x="624" y="234" text-anchor="end">Pete Morrow</text>
  <text class="contact-title" x="624" y="256" text-anchor="end">Editor</text>
  <text class="contact-line" x="624" y="285" text-anchor="end">P.O. Box 5817</text>
  <text class="contact-line" x="618" y="308" text-anchor="end">North Turramurra</text>
  <text class="contact-line" x="624" y="330" text-anchor="end">NSW 2074</text>
  <text class="contact-line" x="624" y="352" text-anchor="end">Ph: 042 735 8819</text>
</svg>

<svg class="card card--radio" viewBox="0 0 646 374" aria-label="Run Loud Radio business card, reverse">
  <defs>
    <radialGradient id="art-tone-back" cx="0" cy="192" r="290" gradientUnits="userSpaceOnUse">
      <stop offset="0" class="stop-red"/>
      <stop offset="0.35" class="stop-red" stop-opacity="0.75"/>
      <stop offset="0.8" class="stop-dark"/>
      <stop offset="1" class="stop-dark"/>
    </radialGradient>
  </defs>
  <rect class="card-bg" width="646" height="374"/>
  <rect x="0" y="0" width="283" height="374" fill="url(#art-tone-back)" role="img" aria-label="Illustration of overlapping vinyl records in black and red"/>
  <path class="art-frame" d="M283 1 L1 1 L1 373 L270 373"/>

  <circle class="wordmark-dot" cx="272" cy="95" r="12"/>
  <text class="wordmark" x="622" y="112" text-anchor="end">Run Loud</text>
  <text class="division division--radio" x="620" y="156" text-anchor="end">RADIO</text>
</svg>

</body>
</html>
```